Rw construct holdings pty ltd

This is a development and construction company. Website can be set up on our domain rwbuildgroup.net if we could change the domain to rwbuildgroup.com.au would be great

Want the page to have eye catching designs, red, black and white are the preffered colours.

Check out www.tolumine.com.au it is my former company with my partner which i am now venturing out on my own, that is the perfect example of the website i want even allot of the information would be the same

Industry/Entity Type

Construction

Coding

Coded - Design and coding required

Number of Pages Required

5+ page

Requirements
Must have
• Company logo eye catching designs

```html
<!DOCTYPE html>
<html lang="en">
<head>
<meta charset="utf-8">
<title>Contact Us – RW Build Group</title>
<link href="https://fonts.googleapis.com/css2?family=Montserrat:wght@400;600;700&family=Open+Sans:wght@400;600&display=swap" rel="stylesheet">
<style>
:root{
  --red:#e8442d;
  --black:#0d0d0d;
  --ink:#222222;
  --muted:#666666;
  --line:#e2e2e2;
  --soft:#f1f1f1;
  --white:#ffffff;
}
*{box-sizing:border-box;margin:0;padding:0}
html,body{width:818px;height:1200px;overflow:hidden;background:var(--white)}
body{font-family:"Open Sans",Arial,sans-serif;color:var(--ink);position:relative}
.header{height:66px;display:flex;align-items:center;justify-content:space-between;padding:0 110px 0 110px}
.brand{display:flex;align-items:center;gap:8px}
.brand-mark{width:14px;height:14px;background:var(--red)}
.brand-name{font-family:"Montserrat",Arial,sans-serif;font-weight:700;font-size:15px;letter-spacing:.5px;color:var(--ink);text-transform:uppercase}
.nav{display:flex;gap:14px;font-family:"Montserrat",Arial,sans-serif;font-size:9px;font-weight:600;text-transform:uppercase}
.nav a{color:var(--ink);text-decoration:none}
.nav a.active{color:var(--red)}
.hero{height:186px;background:linear-gradient(100deg,#6b4a3c 0%,#b59a90 35%,#d9cfcf 60%,#a89595 100%)}
.crumbs{height:28px;border-bottom:1px solid var(--line);display:flex;align-items:center;padding-left:110px;font-family:"Montserrat",Arial,sans-serif;font-size:8px;font-weight:600;text-transform:uppercase;gap:5px}
.crumbs .current{color:var(--red)}
.page-title{text-align:center;font-family:"Montserrat",Arial,sans-serif;font-weight:700;font-size:22px;margin-top:40px}
.intro{display:flex;justify-content:space-between;padding:0 108px;margin-top:20px}
.col{width:275px}
.col h2{font-family:"Montserrat",Arial,sans-serif;font-size:15px;font-weight:700;text-transform:uppercase;margin-bottom:14px}
.col p.lead{font-size:10px;line-height:1.5;color:var(--muted);margin-bottom:14px}
.contact-item{display:flex;align-items:flex-start;gap:12px;margin-bottom:12px}
.contact-icon{width:28px;height:28px;border:1.5px solid var(--ink);border-radius:50%;display:flex;align-items:center;justify-content:center;flex:none}
.contact-item h3{font-family:"Montserrat",Arial,sans-serif;color:var(--red);font-size:10px;font-weight:600}
.contact-item span{font-size:10px;color:var(--muted);line-height:1.4;display:block}
.divider{width:1px;background:var(--line);margin:0 10px}
.map{width:272px;height:100px;background:linear-gradient(135deg,#cfe3c3 0%,#e6e9dc 45%,#c9dcc0 100%)}
.enquiry{position:absolute;top:650px;left:0;width:818px;height:372px;background:var(--soft)}
.enquiry h2{text-align:center;font-family:"Montserrat",Arial,sans-serif;font-weight:700;font-size:18px;margin-top:40px}
.form{width:386px;margin:26px auto 0;display:grid;grid-template-columns:1fr 1fr;gap:8px 12px}
.field{height:30px;background:var(--white);border:1px solid var(--line);font-size:8px;color:var(--muted);padding:0 8px;display:flex;align-items:center;justify-content:space-between}
.field.message{grid-column:1/3;height:92px;align-items:flex-start;padding-top:8px}
.submit{grid-column:1/3;justify-self:center;margin-top:14px;background:var(--red);color:var(--white);font-family:"Montserrat",Arial,sans-serif;font-weight:600;font-size:9px;text-transform:uppercase;padding:9px 14px;letter-spacing:.5px}
.footer{position:absolute;top:1022px;left:0;width:818px;height:178px;background:var(--black);color:var(--white)}
.footer-top{display:flex;align-items:center;gap:14px;padding:0 110px;height:118px}
.footer .brand-name{color:var(--white);font-size:14px;margin-right:24px}
.pill{display:flex;align-items:center;height:22px}
.pill .ico{width:22px;height:22px;background:var(--red);display:flex;align-items:center;justify-content:center}
.pill .txt{background:var(--white);color:var(--ink);font-size:8px;padding:0 8px;height:22px;display:flex;align-items:center}
.socials{display:flex;gap:6px;margin-left:8px}
.socials span{width:20px;height:20px;background:var(--red)}
.footer-bottom{display:flex;justify-content:space-between;padding:0 110px;font-size:8px;border-top:1px solid #2a2a2a;height:60px;align-items:center}
.footer-bottom nav{display:flex;gap:16px}
</style>
</head>
<body>
<header class="header">
  <div class="brand"><span class="brand-mark"></span><span class="brand-name">RW Build Group</span></div>
  <nav class="nav"><a href="#">Home</a><a href="#">About Us</a><a href="#">Services</a><a href="#">Projects</a><a href="#" class="active">Contact Us</a></nav>
</header>
<div class="hero" role="img" aria-label="Photo of a hand holding a smartphone"></div>
<div class="crumbs"><span>Home</span><span>/</span><span class="current">Contact Us</span></div>
<h1 class="page-title">CONTACT US</h1>
<section class="intro">
  <div class="col">
    <h2>Get in touch</h2>
    <p class="lead">Lorem ipsum dolor sit amet, consectetur adipiscing elit sed diam nonummy nibh euismod.</p>
    <div class="contact-item">
      <span class="contact-icon"><svg width="12" height="14" viewBox="0 0 12 14"><path d="M6 1a4.5 4.5 0 0 0-4.5 4.5C1.5 9 6 13 6 13s4.5-4 4.5-7.5A4.5 4.5 0 0 0 6 1z" fill="none" stroke="#e8442d" stroke-width="1.3"/><circle cx="6" cy="5.5" r="1.6" fill="#e8442d"/></svg></span>
      <div><h3>RW Build Group</h3><span>123 Lorem ipsum dolor sit amet<br>consectetur.</span></div>
    </div>
    <div class="contact-item">
      <span class="contact-icon"><svg width="12" height="12" viewBox="0 0 12 12"><path d="M2.5 1h2l1 3-1.4 1a7 7 0 0 0 3 3l1-1.4 3 1v2a1 1 0 0 1-1 1A9.5 9.5 0 0 1 1.5 2a1 1 0 0 1 1-1z" fill="none" stroke="#e8442d" stroke-width="1.2"/></svg></span>
      <div><h3>Phone</h3><span>+1 (234) 555 - 0190</span></div>
    </div>
    <div class="contact-item">
      <span class="contact-icon"><svg width="13" height="10" viewBox="0 0 13 10"><rect x="0.7" y="0.7" width="11.6" height="8.6" fill="none" stroke="#e8442d" stroke-width="1.2"/><path d="M0.7 0.7l5.8 5 5.8-5" fill="none" stroke="#e8442d" stroke-width="1.2"/></svg></span>
      <div><h3>Email</h3><span>info@rwbuildgroup.com.au</span></div>
    </div>
  </div>
  <div class="divider"></div>
  <div class="col">
    <h2>Location map</h2>
    <div class="map" role="img" aria-label="Map showing the office location"></div>
  </div>
</section>
<section class="enquiry">
  <h2>CONTACT US</h2>
  <div class="form">
    <div class="field">Name</div>
    <div class="field">Email</div>
    <div class="field">Phone</div>
    <div class="field">Inquiry For <svg width="7" height="4" viewBox="0 0 7 4"><path d="M0 0h7L3.5 4z" fill="#666"/></svg></div>
    <div class="field message">Message here...</div>
    <div class="submit">Send a message</div>
  </div>
</section>
<footer class="footer">
  <div class="footer-top">
    <span class="brand-name">RW Build Group</span>
    <div class="pill"><span class="ico"><svg width="10" height="10" viewBox="0 0 12 12"><path d="M2.5 1h2l1 3-1.4 1a7 7 0 0 0 3 3l1-1.4 3 1v2a1 1 0 0 1-1 1A9.5 9.5 0 0 1 1.5 2a1 1 0 0 1 1-1z" fill="#fff"/></svg></span><span class="txt">+1 (234) 555 - 0190</span></div>
    <div class="pill"><span class="ico"><svg width="11" height="8" viewBox="0 0 13 10"><rect x="0.7" y="0.7" width="11.6" height="8.6" fill="none" stroke="#fff" stroke-width="1.3"/><path d="M0.7 0.7l5.8 5 5.8-5" fill="none" stroke="#fff" stroke-width="1.3"/></svg></span><span class="txt">info@rwbuildgroup.com.au</span></div>
    <div class="socials"><span></span><span></span><span></span></div>
  </div>
  <div class="footer-bottom">
    <nav><span>Home</span><span>About Us</span><span>Services</span><span>Projects</span><span>Contact Us</span></nav>
    <span>Copyright © 2022 RW Build Group | All Rights Reserved.</span>
  </div>
</footer>
</body>
</html>
```